KELVANE HOMES & ASSOCIATES T.W.P.

I am wanting a classy double sided black standard size card with Metalic Rose gold for both the logo and lettering (name) on the front then my picture and contact info on the back.
The logo has a circle that is a sun symbol and that needs to be in METALIC GOLD AT THE TOP AND CASCADE TO rose gold then the line under it needs to be yellow METALIC gold The lettering on the front also to be Rose gold metalic. The back side with picture and phone # needs to be ROSE gold metalic
INFO FOR BACK OF CARD WITH PICTURE AND BLACK BACK ROUND
front
Mirela Jostad Realtor
back
license 07418923
email | mirela.jostad@kelvanehomes.example
c. 555.218.4790
f. 555.634.0182
web kelvanehomes.example
812 Larkmoor DR. Vista Calif. 92000

Target Market(s)

REAL ESTATE

Industry/Entity Type

REAL ESTATE

Contact Information for Business Card

NAME ON FRONT Mirela Jostad Agent BACK pic in corner with mirela.jostad@kelvanehomes.example

Font styles to use
Serif

Requirements
Must have
• BLACK FRONT AND BACK WITH METALIC ROSE GOLD LETTERING SEE EXAMPLE BELOW IN PICS
Nice to have
• I WOULD LIKE TO HAVE THE LOGO IN ROSE GOLD METALIC AND THE LINE UNDER THE CIRCLE TO BE IN YELLOW metalic GOLD. TO GIVE IT A SUN SET AFFECT ONLY MY NAME AND TITLE ON THE FRONT with a line on top AND THEN MY CONTACT INFO ON THE BACK
Should not have
• COLORS OTHER THAN BLACK , CHARCOLE AND METALIC LETTERS

```html
<!DOCTYPE html>
<html lang="en">
<head>
<meta charset="utf-8">
<title>Kelvane Homes – Mirela Jostad Business Card</title>
<link rel="stylesheet" href="https://fonts.googleapis.com/css2?family=Cinzel:wght@700&family=Questrial&family=Work+Sans:wght@400&display=swap">
<style>
  :root {
    --page: #ffffff;
    --card-dark: #15191e;
    --card-mid: #2e3640;
    --card-glow: #46515e;
    --rose: #ecc9cf;
    --gold: #f2b41c;
    --white: #f3f4f6;
    --icon-rose: #e7b7c0;
    --photo-warm: #6b4a3a;
    --photo-deep: #1e1a1a;
  }
  * { box-sizing: border-box; margin: 0; padding: 0; }
  html, body {
    width: 1200px; height: 900px; overflow: hidden;
    background: var(--page);
  }
  .sheet {
    position: relative; width: 1200px; height: 900px;
    display: flex; align-items: center; justify-content: center; gap: 40px;
  }
  .card {
    position: relative; width: 520px; height: 297px; overflow: hidden;
    background:
      radial-gradient(ellipse 60% 45% at 50% 70%, rgba(70,81,94,0.65), transparent 70%),
      linear-gradient(180deg, var(--card-dark) 0%, var(--card-mid) 45%, var(--card-dark) 100%);
    font-family: "Questrial", sans-serif;
    color: var(--white);
  }

  /* Logo side */
  .brand-name {
    position: absolute; left: 0; right: 0; top: 134px;
    text-align: center;
    font-family: "Cinzel", serif; font-weight: 700;
    font-size: 28px; letter-spacing: 1px; line-height: 36px;
    color: var(--rose); white-space: nowrap;
  }
  .brand-rule {
    position: absolute; left: 133px; width: 254px; top: 185px;
    height: 2px; background: var(--gold);
  }
  .front-name {
    position: absolute; left: 0; right: 0; top: 199px;
    text-align: center; font-size: 22px; line-height: 28px; color: var(--white);
  }

  /* Contact side */
  .portrait {
    position: absolute; left: 13px; top: 12px; width: 233px; height: 234px;
    border-radius: 0 130px 150px 20px / 0 117px 117px 4px;
    background: radial-gradient(ellipse at 45% 45%, var(--photo-warm) 0%, #3c2c26 45%, var(--photo-deep) 100%);
  }
  .agent-name {
    position: absolute; left: 273px; top: 100px;
    font-size: 23px; line-height: 28px; color: var(--gold); white-space: nowrap;
  }
  .agent-title {
    position: absolute; left: 279px; top: 126px; font-size: 15px; line-height: 18px;
  }
  .contact-row {
    position: absolute; display: flex; align-items: center; gap: 7px;
    font-size: 14px; line-height: 18px; white-space: nowrap;
  }
  .contact-row svg { width: 11px; height: 11px; flex: none; }
  .row-mobile { left: 275px; top: 151px; }
  .row-office { left: 266px; top: 173px; }
  .row-email { left: 252px; top: 195px; font-size: 13.5px; }
  .address {
    position: absolute; left: 218px; top: 226px;
    font-family: "Work Sans", sans-serif; font-style: normal;
    font-size: 11.5px; line-height: 15px;
  }
</style>
</head>
<body>
<main class="sheet">
  <section class="card card-front" aria-label="Card front">
    <p class="brand-name">KELVANE HOMES</p>
    <div class="brand-rule"></div>
    <p class="front-name">Mirela Jostad</p>
  </section>

  <section class="card card-back" aria-label="Card back">
    <div class="portrait" role="img" aria-label="Portrait photo of the agent"></div>
    <p class="agent-name">Mirela Jostad</p>
    <p class="agent-title">Agent</p>

    <p class="contact-row row-mobile">
      <svg viewBox="0 0 12 12" aria-hidden="true"><rect x="3" y="0.8" width="6" height="10.4" rx="1.2" fill="none" stroke="var(--icon-rose)" stroke-width="1.3"/><circle cx="6" cy="9.3" r="0.7" fill="var(--icon-rose)"/></svg>
      <span>555.218.4790</span>
    </p>
    <p class="contact-row row-office">
      <svg viewBox="0 0 12 12" aria-hidden="true"><path d="M1 4.5 Q6 1 11 4.5 L10 6 L8 5.2 L8 4 Q6 3.3 4 4 L4 5.2 L2 6 Z" fill="none" stroke="var(--icon-rose)" stroke-width="1"/><rect x="2.5" y="6.5" width="7" height="4.5" rx="1" fill="none" stroke="var(--icon-rose)" stroke-width="1"/><circle cx="6" cy="8.7" r="1" fill="var(--icon-rose)"/></svg>
      <span>555.634-0182</span>
    </p>
    <p class="contact-row row-email">
      <svg viewBox="0 0 12 12" aria-hidden="true"><g fill="none" stroke="var(--icon-rose)" stroke-width="1"><circle cx="6" cy="6" r="5"/><ellipse cx="6" cy="6" rx="2.2" ry="5"/><line x1="1" y1="6" x2="11" y2="6"/><line x1="1.8" y1="3.5" x2="10.2" y2="3.5"/><line x1="1.8" y1="8.5" x2="10.2" y2="8.5"/></g></svg>
      <span>mirela.jostad@kelvanehomes.example</span>
    </p>

    <address class="address">
      812 Larkmoor DR.<br>Vista Calif. 92000
    </address>
  </section>
</main>
</body>
</html>
```